Landing Page for a Social Survey

Hi guys,
we need an elegant landing page for a new project. It's a social survey where users need to answer some questions to participate at a lottery.
I attached an example about what we want. As in the example the design should be very elegant and engage to user to click on the button and take part in the survey.
Also the design should look a bit like lumbrook.
If you have any questions, don't hesitate to ask. I'll try to respond as soon as possible.
Please use the following texts:
Header: "Social Network Umfrage"
Headline above the text: "Herzlichen Glückwunsch"
Text:
"Sie wurden als einer von wenigen Nutzern aus Berlin und Umgebung ausgewählt an unserer Umfrage über Social Networks teilzunehmen.
Die Beantwortung der Fragen dauert nur wenige Sekunden. Als Dankeschön für Ihre Teilnahme können Sie ein Zelvo4, Trenu2 oder Pelwin Slate gewinnen."
Button: "Jetzt teilnehmen"

```html
<!DOCTYPE html>
<html lang="de">
<head>
<meta charset="utf-8">
<title>Social Network Umfrage</title>
<link rel="stylesheet" href="https://fonts.googleapis.com/css2?family=Arimo:wght@700&family=Source+Sans+3:wght@400;600&display=swap">
<style>
  :root {
    --page-light: #f7f9fb;
    --page-edge: #d6dee7;
    --bar-top: #5a7fa6;
    --bar-bottom: #2e5683;
    --bar-border: #244a73;
    --home-tile: #2a4f79;
    --home-icon: #4f7aa7;
    --text-white: #ffffff;
    --body-text: #2b2b2b;
    --link-text: #111111;
    --modal-top: #ffffff;
    --modal-bottom: #d9d9d9;
    --modal-border: #9ea8b2;
    --footer-band: #c9d5e1;
    --footer-text: #6e7680;
    --device-tone: #b9c3cd;
    --device-tone-light: #e3e8ee;
  }
  * { box-sizing: border-box; margin: 0; padding: 0; }
  html, body { width: 1200px; height: 620px; overflow: hidden; }
  body {
    position: relative;
    font-family: "Source Sans 3", sans-serif;
    background: radial-gradient(ellipse 700px 420px at 600px 200px, var(--page-light) 0%, #eaeff4 55%, var(--page-edge) 100%);
  }
  .device-art {
    position: absolute;
    border-radius: 28px;
    opacity: .7;
  }
  .device-art.left {
    left: 100px; top: 60px; width: 320px; height: 490px;
    background: radial-gradient(ellipse at 45% 45%, var(--device-tone) 0%, var(--device-tone-light) 60%, rgba(227,232,238,0) 80%);
  }
  .device-art.right {
    left: 910px; top: 290px; width: 290px; height: 285px;
    background: radial-gradient(ellipse at 60% 45%, var(--device-tone) 0%, var(--device-tone-light) 60%, rgba(227,232,238,0) 80%);
  }
  .top-bar {
    position: absolute; left: 128px; top: 0; width: 944px; height: 41px;
    background: linear-gradient(var(--bar-top), var(--bar-bottom));
    border: 1px solid var(--bar-border); border-top: none;
    border-radius: 0 0 4px 4px;
    display: flex; align-items: center;
  }
  .home-tile {
    width: 49px; height: 40px; background: var(--home-tile);
    display: flex; align-items: center; justify-content: center;
    border-radius: 0 0 0 4px;
  }
  .site-title {
    margin-left: 15px;
    font-family: "Arimo", sans-serif; font-weight: 700; font-size: 20px;
    color: var(--text-white); letter-spacing: .2px;
  }
  .survey-date {
    margin-left: auto; margin-right: 12px;
    font-size: 16px; color: var(--text-white);
  }
  .date-icon { margin-right: 8px; }
  .invite-card {
    position: absolute; left: 313px; top: 129px; width: 574px; height: 313px;
    background: linear-gradient(var(--modal-top) 20%, var(--modal-bottom));
    border: 1px solid var(--modal-border);
    box-shadow: 0 4px 18px rgba(40,60,80,.45);
  }
  .invite-heading {
    height: 36px; padding-left: 23px;
    background: linear-gradient(var(--bar-top), var(--bar-bottom));
    color: var(--text-white); font-size: 21px; font-weight: 600;
    line-height: 36px;
  }
  .invite-body {
    padding: 25px 32px 0 32px;
    font-size: 16.5px; line-height: 21px; color: var(--body-text);
  }
  .invite-body p + p { margin-top: 22px; }
  .prize { color: var(--link-text); text-decoration: underline; }
  .join-button {
    position: absolute; left: 197px; top: 243px; width: 176px; height: 45px;
    border-radius: 4px; border: 1px solid var(--bar-border);
    background: linear-gradient(var(--bar-top), var(--bar-bottom));
    color: var(--text-white); font: 600 19px "Source Sans 3", sans-serif;
    box-shadow: 0 1px 3px rgba(0,0,0,.3);
  }
  .site-footer {
    position: absolute; left: 128px; top: 572px; width: 1072px; height: 36px;
    background: var(--footer-band);
    padding-left: 16px; line-height: 40px;
    font-size: 11px; color: var(--footer-text);
  }
</style>
</head>
<body>
  <div class="device-art left" role="img" aria-label="Faint illustration of a smartphone, laptop and tablet"></div>
  <div class="device-art right" role="img" aria-label="Faint illustration of a smartphone and laptop"></div>

  <header class="top-bar">
    <div class="home-tile">
      <svg width="28" height="24" viewBox="0 0 28 24" aria-hidden="true">
        <path d="M14 2 L27 13 L23 13 L23 23 L17 23 L17 16 L11 16 L11 23 L5 23 L5 13 L1 13 Z" fill="var(--home-icon)"/>
      </svg>
    </div>
    <h1 class="site-title">Social Network Umfrage</h1>
    <span class="survey-date">Juni-30-2011</span>
    <svg class="date-icon" width="34" height="36" viewBox="0 0 34 36" aria-hidden="true">
      <rect x="14" y="14" width="18" height="18" rx="2" fill="#fff" stroke="#8aa" />
      <rect x="14" y="14" width="18" height="5" fill="#3a9a3a"/>
      <circle cx="13" cy="13" r="11" fill="#f2f4f6" stroke="#7d8a96" stroke-width="2"/>
      <path d="M13 6 V13 H18" stroke="#3a4a5a" stroke-width="2" fill="none"/>
    </svg>
  </header>

  <main class="invite-card">
    <h2 class="invite-heading">Herzlichen Glückwunsch</h2>
    <div class="invite-body">
      <p>Sie wurden als einer von wenigen Nutzern aus Berlin und Umgebung ausgewählt an unserer Umfrage über Social Networks teilzunehmen.</p>
      <p>Die Beantwortung der Fragen dauert nur wenige Sekunden.</p>
      <p>Als Dankeschön für Ihre Teilnahme können Sie ein <span class="prize">Zelvo4</span>, <span class="prize">Trenu2</span> oder <span class="prize">Pelwin Slate</span> gewinnen</p>
    </div>
    <button class="join-button" type="button">Jetzt teilnehmen</button>
  </main>

  <footer class="site-footer">2011 pollrewardhub.com All rights reserved.</footer>
</body>
</html>
```